Velomar Placeholder Site for Velomar.net

Design and code a small website to function as a placeholder until a more comprehensive site can be developed.

Use the following site as a source for key info and photos:
www.velomar.org/es
Designer can select and download any images on the site for reuse in this new site. The same goes for text. Everything will be in English.

Target Market(s)

Charity

Industry/Entity Type

Charity

Coding

Coded - Design and coding required

Number of Pages Required

5+ page

Font styles to use
Sans Serif

Requirements
Must have
• HOME PAGE
• + Attractive image and test noting the site is a placeholder for a new sitye currently under development.
• + Text blurb
• THEIR HAPPINESS IS THE BEST REWARD FOR OUR EFFORTS.
• HELP US CARE FOR THEM
• + Nice image taken from current .org site
• SHELTER PAGE
• + What we do
• + Image taken from current .org site
• HOSPITAL PAGE
• + What we do
• COMMUNITY HELP
• + What we do
• EDUCATION
• + What we do
• ABOUT
• + Velomar
• REFERENCE SITE
• www.velomar.org/es
Nice to have
• n/a
Should not have
• n/a

```html
<!DOCTYPE html>
<html lang="en">
<head>
<meta charset="utf-8">
<title>Velomar – Support children</title>
<link href="https://fonts.googleapis.com/css2?family=Open+Sans:wght@300;400;600;700&display=swap" rel="stylesheet">
<style>
:root{
  --red:#e21b23;
  --ink:#222;
  --text:#555;
  --muted:#888;
  --dark:#2b2b2b;
  --darker:#1f1f1f;
  --nav:#2a2a2a;
  --light:#f3f3f3;
  --white:#fff;
}
*{box-sizing:border-box;margin:0;padding:0}
html,body{width:1200px;height:2208px;overflow:hidden}
body{font-family:"Open Sans",Arial,sans-serif;color:var(--text);background:var(--white);font-size:13px;line-height:1.6}
.wrap{width:700px;margin:0 auto;position:relative}
.btn{display:inline-block;background:var(--red);color:var(--white);font-size:12px;font-weight:600;text-transform:uppercase;padding:8px 18px;letter-spacing:.5px;text-decoration:none;white-space:nowrap}
.btn.outline{background:transparent;border:1px solid var(--white)}
.btn.small{font-size:10px;padding:5px 12px}

/* header */
.site-header{height:64px;background:var(--white)}
.site-header .wrap{display:flex;justify-content:space-between;align-items:center;height:64px}
.brand{text-decoration:none}
.brand-name{font-size:28px;font-weight:700;color:var(--red);line-height:1}
.site-header .btn{padding:9px 16px}

.main-nav{height:30px;background:var(--nav)}
.main-nav ul{list-style:none;display:flex;justify-content:center;height:30px;align-items:center}
.main-nav li{margin:0 14px;font-size:11px;font-weight:600;color:var(--white);text-transform:uppercase;letter-spacing:.4px}
.main-nav li.active{color:var(--red)}

/* hero */
.hero{position:relative;height:536px;background:linear-gradient(90deg,#8a5a3e 0%,#b78464 35%,#c7a089 60%,#7a4a35 100%);overflow:hidden}
.hero .photo{position:absolute;inset:0;background:radial-gradient(ellipse at 70% 40%,rgba(240,210,190,.5),transparent 60%),linear-gradient(180deg,rgba(255,255,255,.15),rgba(0,0,0,.25))}
.hero-copy{position:absolute;top:200px;left:0;right:0;text-align:center;color:var(--white)}
.hero-copy h1{font-size:38px;font-weight:300;line-height:1.3;text-shadow:0 1px 3px rgba(0,0,0,.4)}
.hero-copy p{width:560px;margin:8px auto 0;font-size:13px;line-height:1.4;text-shadow:0 1px 2px rgba(0,0,0,.5)}
.hero-copy .btn{margin-top:40px;padding:10px 22px}

/* welcome */
.welcome{height:300px;padding-top:50px}
.welcome .wrap{display:flex;justify-content:space-between}
.welcome-text{width:310px}
.welcome-text h2{font-size:28px;font-weight:400;color:var(--ink);line-height:1.2;margin-bottom:14px}
.welcome-text h2 span{color:var(--red)}
.welcome-text p{font-size:12px;line-height:1.55;margin-bottom:16px}
.welcome-text p b{color:var(--red);font-weight:600}
.video{width:330px;height:190px;position:relative;border:5px solid var(--light);margin-top:4px}
.video .photo{position:absolute;inset:0;background:linear-gradient(135deg,#9fb5b0,#6e7c6b 50%,#b9a58c)}
.video .bar{position:absolute;left:0;right:0;bottom:0;height:18px;background:rgba(0,0,0,.7)}

/* cause cards */
.causes{height:370px;padding-top:22px}
.causes .wrap{display:flex;justify-content:space-between}
.cause{width:224px}
.cause .photo{height:110px}
.cause .box{height:210px;background:var(--dark);color:var(--white);text-align:center;padding:62px 18px 0}
.cause .box h3{font-size:13px;font-weight:400;line-height:1.45;margin-bottom:18px}
.cause.featured .box{background:var(--red)}
.cause.featured .btn{background:var(--darker)}
.cause .btn.small{border:1px solid var(--white)}

/* volunteer */
.volunteer{position:relative;height:320px;background:linear-gradient(90deg,#3a302b,#5a4a40 40%,#2e2824);color:var(--white);text-align:center}
.volunteer::before{content:"";position:absolute;inset:0;background:rgba(0,0,0,.45)}
.volunteer .inner{position:relative;padding-top:68px}
.volunteer h2{font-size:40px;font-weight:300;line-height:1.3}
.volunteer p{font-size:20px;font-weight:300;margin-top:8px}
.volunteer .actions{margin-top:44px;display:flex;justify-content:center;gap:8px}

/* gallery + news */
.lower{height:316px;padding-top:40px}
.lower .wrap{display:flex;justify-content:space-between}
.section-title{font-size:20px;font-weight:400;color:var(--ink);padding-bottom:8px;border-bottom:1px solid #ddd;margin-bottom:24px;line-height:1.4}
.section-title span{color:var(--red)}
.gallery{width:440px}
.thumbs{display:flex;gap:8px}
.thumbs div{width:104px;height:140px}
.news{width:210px}
.news-item{display:flex;gap:10px;margin-bottom:24px}
.date{width:34px;height:40px;background:var(--red);color:var(--white);text-align:center;font-size:13px;font-weight:700;line-height:1.2;padding-top:4px;flex:none}
.date small{display:block;font-size:8px;font-weight:400;background:var(--white);color:var(--red);margin:3px 2px 0}
.news-item h4{font-size:11px;font-weight:600;color:var(--ink)}
.news-item p{font-size:10px;line-height:1.4;color:var(--muted)}

/* footer */
.site-footer{height:224px;background:var(--dark);color:#bbb;padding-top:32px}
.site-footer .wrap{display:flex;justify-content:space-between}
.col h5{font-size:13px;font-weight:400;color:var(--white);margin-bottom:12px}
.col ul{list-style:none}
.col li{font-size:10px;line-height:2;padding-left:10px;position:relative}
.col li::before{content:"";position:absolute;left:0;top:8px;width:4px;height:4px;background:var(--red)}
.col li.on{color:var(--red)}
.menu-col{width:130px}.info-col{width:140px}.contact-col{width:160px}.quick-col{width:150px}
.contact-row{display:flex;gap:8px;font-size:10px;line-height:1.4;margin-bottom:12px}
.contact-row svg{flex:none}
.field{height:22px;background:#3c3c3c;border:1px solid #4a4a4a;margin-bottom:8px;font-size:9px;color:#888;padding:3px 8px}
.field.area{height:34px}
.quick-col .btn{margin-top:2px}
.bottom-bar{height:48px;background:var(--darker)}
.bottom-bar .wrap{display:flex;justify-content:space-between;align-items:center;height:48px;font-size:10px;color:#888}
.social{display:flex;gap:6px}
.social span{width:18px;height:18px;border-radius:50%;background:#555}
</style>
</head>
<body>

<header class="site-header">
  <div class="wrap">
    <a class="brand" href="#"><span class="brand-name">Velomar</span></a>
    <a class="btn" href="#">Donate Now</a>
  </div>
</header>
<nav class="main-nav">
  <ul>
    <li class="active">Home</li><li>About</li><li>Shelter</li><li>Hospital</li><li>Community</li><li>Education</li><li>Contact Us</li>
  </ul>
</nav>

<section class="hero">
  <div class="photo" role="img" aria-label="Photo of smiling children in a schoolyard"></div>
  <div class="hero-copy">
    <h1>Support children in making their career</h1>
    <p>Their happiness is the best reward for our efforts. This site is a placeholder while our new website is under development.</p>
    <a class="btn" href="#">Read More</a>
  </div>
</section>

<section class="welcome">
  <div class="wrap">
    <div class="welcome-text">
      <h2>Welcome <span>Our Company</span></h2>
      <p>We save <b>orphans and abandoned</b> children from the streets and poverty. We feed them, give them shelter, dress them and care for their health and education, away from the hunger, malnutrition and disease around them.</p>
      <a class="btn small" href="#">View More</a>
    </div>
    <div class="video">
      <div class="photo" role="img" aria-label="Video still of children at the shelter"></div>
      <div class="bar"></div>
    </div>
  </div>
</section>

<section class="causes">
  <div class="wrap">
    <article class="cause">
      <div class="photo" role="img" aria-label="Photo of children at a water pump" style="background:linear-gradient(160deg,#8fa9b8,#b6a37e 60%,#7d6a4c)"></div>
      <div class="box"><h3>Help African children<br>to get shelter</h3><a class="btn small" href="#">Donate Now</a></div>
    </article>
    <article class="cause featured">
      <div class="photo" role="img" aria-label="Photo of children in a classroom" style="background:linear-gradient(160deg,#c9a58a,#8a5f48 55%,#5d7fa0)"></div>
      <div class="box"><h3>Help African children<br>to get Education</h3><a class="btn small" href="#">Donate Now</a></div>
    </article>
    <article class="cause">
      <div class="photo" role="img" aria-label="Photo of a doctor caring for a child" style="background:linear-gradient(160deg,#d8d3cc,#a88a72 55%,#6e5545)"></div>
      <div class="box"><h3>Free medical care<br>treatment and medicines</h3><a class="btn small" href="#">Donate Now</a></div>
    </article>
  </div>
</section>

<section class="volunteer" role="img" aria-label="Background photo of children, darkened">
  <div class="inner">
    <h2>Are you ready to volunteer?</h2>
    <p>start one of our programm today and help people in need</p>
    <div class="actions"><a class="btn" href="#">Become a Volunteer</a><a class="btn outline" href="#">Make a Donation</a></div>
  </div>
</section>

<section class="lower">
  <div class="wrap">
    <div class="gallery">
      <h3 class="section-title">Photo <span>Gallery</span></h3>
      <div class="thumbs">
        <div role="img" aria-label="Gallery photo of a child" style="background:linear-gradient(150deg,#c4a98e,#7a5a44)"></div>
        <div role="img" aria-label="Gallery photo of children playing" style="background:linear-gradient(150deg,#d05a4c,#8a4a3a)"></div>
        <div role="img" aria-label="Gallery photo of a group of children" style="background:linear-gradient(150deg,#b7a98f,#6e6152)"></div>
        <div role="img" aria-label="Gallery photo of children outdoors" style="background:linear-gradient(150deg,#a9b4a0,#6a5a4a)"></div>
      </div>
    </div>
    <div class="news">
      <h3 class="section-title">Latest <span>News</span></h3>
      <div class="news-item"><div class="date">26<small>NOV</small></div><div><h4>New Valley 3 goal</h4><p>Lorem ipsum text here for volunteer's news</p></div></div>
      <div class="news-item"><div class="date">24<small>NOV</small></div><div><h4>News Headlines Here</h4><p>Lorem ipsum text here for volunteer's news</p></div></div>
    </div>
  </div>
</section>

<footer class="site-footer">
  <div class="wrap">
    <div class="col menu-col">
      <h5>Main menu</h5>
      <ul><li class="on">Home</li><li>About Us</li><li>Shelter</li><li>Community</li><li>Education</li></ul>
    </div>
    <div class="col info-col">
      <h5>Information</h5>
      <ul><li>Donations</li><li>Legal Notice</li><li>Terms and conditions</li><li>Become a volunteer</li><li>Contact us</li></ul>
    </div>
    <div class="col contact-col">
      <h5>Contact us</h5>
      <div class="contact-row"><svg width="14" height="14" viewBox="0 0 14 14"><path d="M7 1a4 4 0 0 0-4 4c0 3 4 8 4 8s4-5 4-8a4 4 0 0 0-4-4z" fill="#bbb"/><circle cx="7" cy="5" r="1.5" fill="#2b2b2b"/></svg><span>Velomar Foundation<br>Calle Mayor 12, 28013 Madrid</span></div>
      <div class="contact-row"><svg width="14" height="14" viewBox="0 0 14 14"><path d="M3 1h3l1 3-2 1a7 7 0 0 0 4 4l1-2 3 1v3a1 1 0 0 1-1 1A11 11 0 0 1 2 2a1 1 0 0 1 1-1z" fill="#bbb"/></svg><span>+34 911 204 380</span></div>
      <div class="contact-row"><svg width="14" height="14" viewBox="0 0 14 14"><rect x="1" y="3" width="12" height="8" fill="none" stroke="#bbb"/><path d="M1 3l6 5 6-5" fill="none" stroke="#bbb"/></svg><span>velomar@velomar.org</span></div>
    </div>
    <div class="col quick-col">
      <h5>Quick Contact</h5>
      <div class="field">Your name</div>
      <div class="field">Email</div>
      <div class="field area">Message</div>
      <a class="btn small" href="#">Submit</a>
    </div>
  </div>
</footer>
<div class="bottom-bar">
  <div class="wrap">
    <span>© 2014 Velomar . All right reserved</span>
    <div class="social"><span></span><span></span><span></span><span></span><span></span><span></span></div>
  </div>
</div>

</body>
</html>
```